Tradeshow display - back drop and matching podium wrap

Looking for a design for a tradeshow display 136.22" x 90.55". and there is approximately 12.25" side panels on each side here (see attached). Needs design for matching podium wrap as well (specs attached).
You can take a look at our website to get a feel on who we are.
www.brindlecrestflow.com
I've added a design I like so you get an idea of what I'm wanting here.
We do not want the Lumora logos on the banner please.
We do water treatment using ozone.

Industry/Entity Type

Agriculture

Requirements
Should not have
• the lumora logos

```html
<!DOCTYPE html>
<html lang="en">
<head>
<meta charset="utf-8">
<title>Brindlecrest Flow – Tradeshow Backdrop and Podium Wrap</title>
<link rel="stylesheet" href="https://fonts.googleapis.com/css2?family=Jost:wght@500;600;700&family=Roboto:wght@400;500&display=swap">
<style>
  :root {
    --stage: #5f5f5f;
    --paper: #ffffff;
    --paper-shade: #eef1f4;
    --brand-blue: #0b5fb0;
    --deep-blue: #1450a8;
    --water-light: #1aa0e0;
    --water-mid: #0a86cc;
    --water-deep: #0672b8;
    --text-light: #ffffff;
  }
  * { box-sizing: border-box; margin: 0; padding: 0; }
  html, body {
    width: 1200px;
    height: 840px;
    overflow: hidden;
    background: var(--stage);
  }
  .canvas {
    position: relative;
    width: 1200px;
    height: 840px;
  }

  /* shared panel pieces */
  .panel { position: absolute; overflow: hidden; background: var(--paper); }
  .panel-art { position: absolute; inset: 0; width: 100%; height: 100%; }
  .brand-name {
    position: absolute;
    left: 0; right: 0;
    text-align: center;
    font-family: "Jost", sans-serif;
    font-weight: 700;
    color: var(--brand-blue);
    line-height: 0.95;
    letter-spacing: -0.01em;
  }
  .web-address {
    position: absolute;
    left: 0; right: 0;
    text-align: center;
    color: var(--text-light);
  }

  /* backdrop */
  .backdrop {
    left: 420px; top: 110px;
    width: 740px; height: 640px;
  }
  .backdrop .brand-name {
    top: 78px;
    left: -40px;
    font-size: 84px;
  }
  .tagline {
    position: absolute;
    left: 0; right: 40px;
    top: 418px;
    text-align: center;
    font-family: "Jost", sans-serif;
    font-weight: 500;
    font-size: 42px;
    line-height: 1.3;
    color: var(--text-light);
  }
  .tagline .quote-mark {
    color: var(--deep-blue);
    font-weight: 700;
    font-size: 56px;
    line-height: 0;
  }
  .tagline .quote-open { position: relative; top: -14px; margin-right: 6px; }
  .tagline .quote-close { position: relative; top: 10px; margin-left: 4px; }
  .backdrop .web-address {
    top: 566px;
    right: 40px;
    font-family: "Roboto", sans-serif;
    font-weight: 500;
    font-size: 15px;
    letter-spacing: 0.2em;
  }

  /* podium wrap */
  .podium-wrap {
    left: 80px; top: 400px;
    width: 270px; height: 330px;
  }
  .podium-wrap .brand-name {
    top: 42px;
    font-size: 36px;
  }
  .podium-wrap .web-address {
    top: 282px;
    font-family: "Roboto", sans-serif;
    font-size: 11px;
    letter-spacing: 0.02em;
  }
</style>
</head>
<body>
<main class="canvas">

  <section class="panel backdrop" aria-label="Tradeshow backdrop">
    <svg class="panel-art" viewBox="0 0 740 640" preserveAspectRatio="none">
      <defs>
        <linearGradient id="droplet-field" x1="0" y1="0" x2="1" y2="1">
          <stop offset="0" stop-color="#ffffff"/>
          <stop offset="0.5" stop-color="#f3f5f7"/>
          <stop offset="1" stop-color="#ffffff"/>
        </linearGradient>
        <linearGradient id="water-field" x1="0" y1="0" x2="0.3" y2="1">
          <stop offset="0" stop-color="#1aa0e0"/>
          <stop offset="0.45" stop-color="#0a86cc"/>
          <stop offset="1" stop-color="#0a93d8"/>
        </linearGradient>
      </defs>
      <rect width="740" height="640" fill="url(#droplet-field)" role="img" aria-label="Soft texture of water droplets on white"/>
      <path class="wave-water" role="img" aria-label="Blue water surface with gentle ripples"
            d="M0,300 C70,250 170,245 255,292 C335,336 425,342 505,302 C595,256 675,214 740,198 L740,640 L0,640 Z"
            fill="url(#water-field)"/>
      <path class="wave-band" d="M0,300 C70,250 170,245 255,292" fill="none" stroke="var(--deep-blue)" stroke-width="10"/>
      <path class="wave-band-inner" d="M0,318 C70,268 170,262 250,306" fill="none" stroke="#ffffff" stroke-width="5"/>
      <path class="wave-line" d="M262,262 C330,320 390,330 460,304 C565,266 655,178 740,146" fill="none" stroke="var(--deep-blue)" stroke-width="4"/>
      <path class="wave-edge" d="M255,292 C335,336 425,342 505,302 C595,256 675,214 740,198" fill="none" stroke="var(--deep-blue)" stroke-width="5"/>
    </svg>

    <h1 class="brand-name">Brindlecrest<br>Flow</h1>

    <p class="tagline">
      <span class="quote-mark quote-open">&ldquo;</span>High Quality Water Just<br>
      Makes Good Sense<span class="quote-mark quote-close">&rdquo;</span>
    </p>

    <p class="web-address">www.brindlecrestflow.com</p>
  </section>

  <section class="panel podium-wrap" aria-label="Podium wrap">
    <svg class="panel-art" viewBox="0 0 270 330" preserveAspectRatio="none">
      <rect width="270" height="330" fill="url(#droplet-field)" role="img" aria-label="Soft texture of water droplets on white"/>
      <path class="wave-water" role="img" aria-label="Blue water surface with gentle ripples"
            d="M0,232 C40,208 90,206 130,220 C175,236 215,228 270,196 L270,330 L0,330 Z"
            fill="url(#water-field)"/>
      <path class="wave-band" d="M0,232 C40,208 90,206 130,220" fill="none" stroke="var(--deep-blue)" stroke-width="4"/>
      <path class="wave-line" d="M110,210 C150,232 200,222 270,186" fill="none" stroke="var(--deep-blue)" stroke-width="2.5"/>
      <path class="wave-edge" d="M130,220 C175,236 215,228 270,196" fill="none" stroke="var(--deep-blue)" stroke-width="3"/>
    </svg>

    <h2 class="brand-name">Brindlecrest<br>Flow</h2>

    <p class="web-address">www.brindlecrestflow.com</p>
  </section>

</main>
</body>
</html>
```